Western Canadian Survey Company needs Business Card and Letter Head Design

Hello,

We're looking to have our business cards redesigned along with our letterhead.

We've recently changed out logo and would like to use this. Please use some creativity and propose different options (Traditional and modern).

We will provide as much feedback as possible.

Business card should be double sided with our logo. We would also like room for cell phone number, email address and position. Back of the card can just be our logo or potentially a list of our services we provide.

Industry/Entity Type

Business

Contact Information for Business Card

```html
<!DOCTYPE html>
<html lang="en">
<head>
<meta charset="utf-8">
<title>Ridgeline Field Surveys – Stationery</title>
<link rel="stylesheet" href="https://fonts.googleapis.com/css2?family=Michroma&family=Open+Sans:wght@400&display=swap">
<style>
  :root {
    --canvas: #d2d3d5;
    --paper: #ffffff;
    --slate: #587a8b;
    --slate-text: #557889;
    --ink: #1f2326;
    --watermark: #e8ebef;
    --shadow: rgba(60, 40, 40, 0.35);
  }
  * { margin: 0; padding: 0; box-sizing: border-box; }
  html, body { width: 1200px; height: 830px; overflow: hidden; }
  body { background: var(--canvas); position: relative; font-family: "Open Sans", sans-serif; color: var(--ink); }

  .sheet { position: absolute; background: var(--paper); box-shadow: 10px 12px 14px var(--shadow); }

  .card { width: 438px; height: 250px; left: 108px; }
  .card-front { top: 133px; }
  .card-back { top: 458px; background: var(--slate); }
  .letterhead { left: 590px; top: 70px; width: 494px; height: 638px; }

  .brand { position: absolute; display: flex; align-items: center; gap: 8px;
           font-family: "Michroma", sans-serif; color: var(--ink); white-space: nowrap; }
  .brand-square { width: 18px; height: 18px; background: currentColor; flex: none; }

  .card-front .brand { left: 20px; top: 34px; font-size: 13px; }
  .card-back .brand { left: 196px; top: 40px; font-size: 28px; color: var(--paper); }
  .card-back .brand-square { width: 28px; height: 28px; }
  .letterhead .brand { left: 18px; top: 40px; font-size: 15px; }

  .holder { position: absolute; right: 20px; top: 166px; text-align: right; }
  .holder-name { font-family: "Michroma", sans-serif; font-size: 15px; color: var(--slate-text); line-height: 1; }
  .holder-role { font-size: 10px; margin-top: 4px; letter-spacing: 0.2px; }
  .rule { position: absolute; left: 20px; top: 195px; width: 342px; height: 2px; background: var(--slate-text); }

  .contact { position: absolute; left: 20px; list-style: none; font-size: 10.5px; line-height: 14px; }
  .card-front .contact { top: 203px; }
  .letterhead .contact { top: 598px; }
  .contact li { display: flex; align-items: center; gap: 7px; }
  .contact svg { width: 8px; height: 8px; fill: none; stroke: var(--slate-text); stroke-width: 1.4; }

  .services { position: absolute; left: 31px; top: 165px; list-style: none;
              color: var(--paper); font-size: 11px; line-height: 17px; }

  .header-rule { position: absolute; left: 0; right: 0; top: 95px; height: 4px;
                 border-top: 1px solid var(--slate); border-bottom: 1px solid var(--slate); }

  .watermark { position: absolute; left: 90px; top: 330px; font-family: "Michroma", sans-serif;
               font-size: 84px; line-height: 1; color: var(--watermark); }
</style>
</head>
<body>

  <section class="sheet card card-front" aria-label="Business card front">
    <div class="brand"><span class="brand-square"></span>RIDGELINE FIELD SURVEYS LTD</div>
    <div class="holder">
      <p class="holder-name">MAREK ELLISON</p>
      <p class="holder-role">DIRECTOR</p>
    </div>
    <div class="rule"></div>
    <ul class="contact">
      <li><svg viewBox="0 0 10 10"><path d="M2 1 L4 1 L4.5 3 L3.3 4 Q4.5 6 6 6.7 L7 5.5 L9 6 L9 8 Q5 9 1 3 Z"/></svg>+1 250 555-0148</li>
      <li><svg viewBox="0 0 10 10"><rect x="1" y="2" width="8" height="6"/><path d="M1 2 L5 5.5 L9 2"/></svg>info@ridgelinefieldsurveys.com</li>
    </ul>
  </section>

  <section class="sheet card card-back" aria-label="Business card back">
    <div class="brand"><span class="brand-square"></span>RFSL</div>
    <ul class="services">
      <li>QA/QC &amp; Survey Control</li>
      <li>Construction Surveys</li>
      <li>Underground Utility Location</li>
      <li>GIS / Drafting</li>
    </ul>
  </section>

  <section class="sheet letterhead" aria-label="Letterhead">
    <div class="brand"><span class="brand-square"></span>RIDGELINE FIELD SURVEYS LTD</div>
    <div class="header-rule"></div>
    <div class="watermark" aria-hidden="true">RFSL</div>
    <ul class="contact">
      <li><svg viewBox="0 0 10 10"><path d="M2 1 L4 1 L4.5 3 L3.3 4 Q4.5 6 6 6.7 L7 5.5 L9 6 L9 8 Q5 9 1 3 Z"/></svg>+1 250 555-0148</li>
      <li><svg viewBox="0 0 10 10"><rect x="1" y="2" width="8" height="6"/><path d="M1 2 L5 5.5 L9 2"/></svg>info@ridgelinefieldsurveys.com</li>
    </ul>
  </section>

</body>
</html>
```